Business card design needed for a security services business.

We provide a wide range of security services from guard personnel to electronic systems.

Industry/Entity Type

Security Industry

Contact Information for Business Card

Brent Holloway, Owner Office: 780.555.0148; Cell: 780.555.0193 Email: brent@norcrestwatchgroup.example; Address 20487 163 St Edmonton, AB T5X 2K8

Colors
0054AA
0677BA
7BADD7
CADEEF
E8F1F8

Requirements
Nice to have
• On the back of the card I would like to possible list the services I provide: Guards Mobiles Live Video Surveillance Access Intrusion

```html
<!DOCTYPE html>
<html lang="en">
<head>
<meta charset="utf-8">
<title>Norcrest Watch Group – Business Card</title>
<link href="https://fonts.googleapis.com/css2?family=Barlow:wght@400;500;600;700&display=swap" rel="stylesheet">
<style>
  :root {
    --page-bg: #d0d0d0;
    --brand-blue: #0670bc;
    --brand-deep: #0054aa;
    --brand-light: #7badd7;
    --card-white: #ffffff;
    --text-grey: #5a5a5a;
    --rule-grey: #4a4a4a;
  }
  * { margin: 0; padding: 0; box-sizing: border-box; }
  html, body {
    width: 1200px; height: 1000px; overflow: hidden;
    background: var(--page-bg);
    font-family: "Barlow", Arial, sans-serif;
  }
  .canvas { position: relative; width: 1200px; height: 1000px; }
  .card {
    position: absolute; top: 168px;
    width: 353px; height: 612px;
    border-radius: 28px; overflow: hidden;
  }
  .card-back { left: 195px; background: var(--brand-blue); }
  .card-front { left: 642px; background: var(--card-white); }

  .back-pattern {
    position: absolute; inset: 0;
    background:
      repeating-linear-gradient(180deg, rgba(123,173,215,0.18) 0 14px, rgba(0,84,170,0.12) 14px 44px),
      linear-gradient(160deg, #0a78c4 0%, var(--brand-blue) 55%, #0466b0 100%);
  }
  .service-list {
    position: absolute; left: 0; right: 0; top: 486px;
    text-align: center; color: #fff;
    font-weight: 600; font-size: 14px; line-height: 17px;
    text-shadow: 0 1px 2px rgba(0,0,0,0.45);
  }

  .company-name {
    position: absolute; left: 0; right: 0; top: 100px;
    text-align: center; color: var(--brand-blue);
    font-weight: 700; font-size: 30px; line-height: 34px; letter-spacing: 0.5px;
  }
  .person {
    position: absolute; left: 0; right: 0; top: 318px; text-align: center;
  }
  .person-name { color: var(--brand-blue); font-weight: 700; font-size: 23px; line-height: 28px; }
  .person-role { color: var(--text-grey); font-weight: 400; font-size: 21px; line-height: 26px; }

  .contact-divider { position: absolute; left: 50px; top: 393px; }
  .contact-lines {
    position: absolute; left: 0; right: 0; top: 433px;
    text-align: center; color: var(--text-grey);
    font-size: 16.5px; line-height: 22px;
  }
  .short-rule {
    position: absolute; left: 140px; top: 515px;
    width: 78px; height: 2px; background: var(--rule-grey);
  }
  .address {
    position: absolute; left: 0; right: 0; top: 532px;
    text-align: center; color: var(--text-grey);
    font-size: 16.5px; line-height: 22px;
  }
</style>
</head>
<body>
<main class="canvas">

  <section class="card card-back">
    <div class="back-pattern" role="img" aria-label="Repeating brand mark pattern in tonal blue"></div>
    <p class="service-list">Card Access Systems | Mobile Patrols<br>Security Guards | Video Surveillance Systems</p>
  </section>

  <section class="card card-front">
    <h1 class="company-name">NORCREST WATCH<br>GROUP</h1>

    <div class="person">
      <p class="person-name">Brent Holloway</p>
      <p class="person-role">Owner</p>
    </div>

    <svg class="contact-divider" width="260" height="30" viewBox="0 0 260 30" aria-hidden="true">
      <line x1="0" y1="15" x2="80" y2="15" stroke="#4a4a4a" stroke-width="2"/>
      <line x1="180" y1="15" x2="260" y2="15" stroke="#4a4a4a" stroke-width="2"/>
      <!-- office phone -->
      <circle cx="98" cy="15" r="13.5" fill="#0670bc"/>
      <path d="M89 13 q9 -7 18 0 l-1.5 2.5 -3.5 -1 0 -1.5 q-4 -1.5 -8 0 l0 1.5 -3.5 1z" fill="#fff"/>
      <rect x="91.5" y="15" width="13" height="6.5" rx="1.5" fill="#fff"/>
      <circle cx="98" cy="18.2" r="1.8" fill="#0670bc"/>
      <!-- mobile -->
      <circle cx="130" cy="15" r="13.5" fill="#0670bc"/>
      <rect x="125" y="6" width="10" height="18" rx="2" fill="#fff"/>
      <rect x="126.8" y="8.5" width="6.4" height="11.5" fill="#0670bc"/>
      <circle cx="130" cy="22" r="1" fill="#0670bc"/>
      <!-- email -->
      <circle cx="162" cy="15" r="13.5" fill="#0670bc"/>
      <rect x="153" y="9" width="18" height="12" rx="1" fill="#fff"/>
      <path d="M153.5 9.5 l8.5 7 8.5 -7" fill="none" stroke="#0670bc" stroke-width="1.4"/>
    </svg>

    <p class="contact-lines">780.555.0148<br>780.555.0193<br>brent@norcrestwatchgroup.example</p>
    <div class="short-rule"></div>
    <p class="address">20487 163 St Edmonton,<br>AB T5X 2K8</p>
  </section>

</main>
</body>
</html>
```